We need a design for business cards for our new company. We are a resident safety and security company company that focuses on senior living communities. we provide Nurse call, Access control, CCTV, Wired and wireless network infrastructure, Wander Management, and much more!

Our logo is the circuit board shield. Representing our high tech security solutions. I would like the business card to bring the same theme with perhaps some circuit board traces around the card similar to our logo

```html
<!DOCTYPE html>
<html lang="en">
<head>
<meta charset="UTF-8">
<title>ElderNova Business Card</title>
<link rel="stylesheet" href="https://fonts.googleapis.com/css2?family=Libre+Baskerville:wght@400;700&family=Montserrat:wght@400;500;700&display=swap">
<style>
  :root {
    --stage: #d9d9d9;
    --card-white: #ffffff;
    --brand-blue: #2a57b3;
    --brand-deep: #2d5db5;
    --brand-sky: #3cb6ea;
    --ink: #2b2f3a;
    --trace-tint: #eef2f8;
    --white: #ffffff;
  }
  * { box-sizing: border-box; margin: 0; padding: 0; }
  html, body { width: 1200px; height: 802px; overflow: hidden; }
  body {
    background: var(--stage);
    font-family: "Montserrat", sans-serif;
    position: relative;
  }
  .card {
    position: absolute;
    top: 246px;
    width: 540px;
    height: 310px;
    border-radius: 16px;
    overflow: hidden;
    box-shadow: 0 6px 18px rgba(0,0,0,0.18);
  }
  /* Front */
  .card--front { left: 40px; background: var(--card-white); }
  .front__traces {
    position: absolute; right: 0; bottom: 0; width: 330px; height: 120px;
    background: linear-gradient(160deg, rgba(238,242,248,0) 0%, var(--trace-tint) 60%);
  }
  .brand-mark {
    position: absolute; top: 34px; right: 36px;
    display: flex; flex-direction: column; align-items: center; gap: 10px;
  }
  .brand-mark__dot {
    width: 62px; height: 62px; border-radius: 50%;
    background: var(--brand-blue);
  }
  .brand-mark__name {
    font-family: "Libre Baskerville", serif;
    font-size: 24px; color: var(--brand-blue); letter-spacing: 0.5px;
  }
  .person {
    position: absolute; left: 0; top: 142px; padding-left: 30px;
  }
  .person__tab {
    position: absolute; left: 0; top: 4px; width: 10px; height: 30px;
    background: var(--brand-blue);
  }
  .person__name {
    font-family: "Libre Baskerville", serif; font-weight: 700;
    font-size: 21px; color: var(--brand-blue); letter-spacing: 0.5px;
  }
  .person__role { font-size: 13px; color: var(--ink); margin-top: 2px; }
  .contact { list-style: none; margin-top: 22px; }
  .contact__item {
    display: flex; align-items: center; gap: 8px;
    font-size: 14px; color: var(--ink); line-height: 23px;
  }
  .contact__icon { width: 12px; height: 12px; fill: var(--brand-blue); flex: none; }
  /* Back */
  .card--back {
    left: 620px;
    background: linear-gradient(45deg, var(--brand-sky) 0%, #2f7fd0 40%, var(--brand-deep) 100%);
    color: var(--white); text-align: center;
  }
  .back__traces {
    position: absolute; inset: 0;
    background: radial-gradient(ellipse at 50% 40%, rgba(255,255,255,0.06), rgba(255,255,255,0) 70%);
  }
  .back__brand { position: relative; padding-top: 34px; display: flex; flex-direction: column; align-items: center; gap: 10px; }
  .back__dot { width: 70px; height: 70px; border-radius: 50%; background: var(--white); }
  .back__name { font-family: "Libre Baskerville", serif; font-size: 27px; letter-spacing: 0.5px; }
  .services { position: relative; margin-top: 14px; padding: 0 30px; }
  .services__heading {
    display: flex; align-items: center; gap: 12px;
    font-weight: 700; font-size: 15px; letter-spacing: 0.5px;
  }
  .services__heading::before, .services__heading::after {
    content: ""; flex: 1; height: 1px; background: var(--white);
  }
  .services__list { list-style: none; margin-top: 8px; font-size: 13px; line-height: 21px; }
</style>
</head>
<body>
  <section class="card card--front" aria-label="Card front">
    <div class="front__traces" role="img" aria-label="Faint circuit board trace pattern"></div>
    <div class="brand-mark">
      <span class="brand-mark__dot"></span>
      <span class="brand-mark__name">ElderNova</span>
    </div>
    <div class="person">
      <span class="person__tab"></span>
      <h1 class="person__name">MARK ELLISON</h1>
      <p class="person__role">President</p>
      <ul class="contact">
        <li class="contact__item"><svg class="contact__icon" viewBox="0 0 12 12"><path d="M2 1l2 0 1 3-1.3 1a6 6 0 003.3 3.3L8 7l3 1v2a1 1 0 01-1 1A9 9 0 011 2a1 1 0 011-1z"/></svg>(555) 014-2290</li>
        <li class="contact__item"><svg class="contact__icon" viewBox="0 0 12 12"><path d="M3 0h6a1 1 0 011 1v10a1 1 0 01-1 1H3a1 1 0 01-1-1V1a1 1 0 011-1zm0 2v7h6V2z"/></svg>(555) 017-3364</li>
        <li class="contact__item"><svg class="contact__icon" viewBox="0 0 12 12"><path d="M0 2h12v8H0zm1 1l5 4 5-4z"/></svg>Mark@ElderNova.com</li>
        <li class="contact__item"><svg class="contact__icon" viewBox="0 0 12 12"><circle cx="6" cy="6" r="6"/></svg>www.ElderNova.com</li>
      </ul>
    </div>
  </section>

  <section class="card card--back" aria-label="Card back">
    <div class="back__traces" role="img" aria-label="Circuit board trace pattern across the card"></div>
    <div class="back__brand">
      <span class="back__dot"></span>
      <span class="back__name">ElderNova</span>
    </div>
    <div class="services">
      <h2 class="services__heading">OUR SERVICES</h2>
      <ul class="services__list">
        <li>Design - Install - Maintain</li>
        <li>• Wired and Wireless Nurse Call &nbsp;• Access Control &nbsp;• CCTV</li>
        <li>• Network Infrastructure &nbsp;• Wander Management</li>
      </ul>
    </div>
  </section>
</body>
</html>
```